Velorine Jewellery Display Card

We are a jewellery manufacturer and need artwork for an A4 size strut card to advertise our new "Crescent Loop Pendant "
In the attached files is a picture of the new pendant and artwork for our trademark "Velorine"
We also need to include the phrase " an expression of love "
as part of the artwork.
The background colour should be predominately white

Target Market(s)

This product has been designed as a gift for Mothers as it has their children names
engraved on the pendant

Industry/Entity Type

Manufacturer

Font styles to use
Serif
Script

Colors
ffffff

Requirements
Must have
• Artwork should be simple and elegant , the predominant look in Australian jewellery stores which is where these display cards will be is white, bright and elegant

```html
<!DOCTYPE html>
<html lang="en">
<head>
<meta charset="utf-8">
<title>Velorine – An Expression of Love</title>
<link rel="stylesheet" href="https://fonts.googleapis.com/css2?family=Lato:wght@300&family=Amatic+SC:wght@400&display=swap">
<style>
  :root {
    --mat: #000000;
    --card: #ffffff;
    --brand-grey: #a3a5a8;
    --love-pink: #e61e6e;
    --silver-light: #f4f5f7;
    --silver-mid: #d2d4d8;
    --heart-grey: #dcdde1;
  }
  html, body {
    margin: 0;
    padding: 0;
    overflow: hidden;
    background: var(--mat);
  }
  .canvas {
    position: relative;
    width: 1200px;
    height: 1153px;
    background: var(--mat);
    overflow: hidden;
  }
  .display-card {
    position: absolute;
    left: 132px;
    top: 230px;
    width: 936px;
    height: 692px;
    background: var(--card);
    overflow: hidden;
  }
  .brand-name {
    position: absolute;
    left: 600px;
    top: 50px;
    width: 270px;
    margin: 0;
    font-family: "Lato", sans-serif;
    font-weight: 300;
    font-size: 50px;
    line-height: 1;
    letter-spacing: 4px;
    color: var(--brand-grey);
    white-space: nowrap;
  }
  .tagline {
    position: absolute;
    left: 44px;
    top: 206px;
    width: 420px;
    margin: 0;
    font-family: "Amatic SC", cursive;
    font-weight: 400;
    font-size: 112px;
    line-height: 94px;
    text-align: center;
    color: var(--love-pink);
    white-space: nowrap;
  }
  .tagline span { display: block; }
  .tagline .line-short { margin-left: -14px; }
  .pendant-photo {
    position: absolute;
    left: 496px;
    top: 192px;
    width: 268px;
    height: 350px;
  }
  .hearts-band {
    position: absolute;
    left: 88px;
    top: 500px;
    width: 848px;
    height: 192px;
  }
</style>
</head>
<body>
<main class="canvas">
  <section class="display-card">
    <h1 class="brand-name">VELORINE</h1>

    <h2 class="tagline">
      <span>AN</span>
      <span>EXPRESSION</span>
      <span class="line-short">OF LOVE</span>
    </h2>

    <svg class="pendant-photo" role="img" aria-label="Silver Crescent Loop Pendant with tree of life centre and engraved children's names" viewBox="0 0 268 350">
      <defs>
        <radialGradient id="silverTone" cx="50%" cy="40%" r="62%">
          <stop offset="0%" stop-color="var(--silver-light)"/>
          <stop offset="100%" stop-color="var(--silver-mid)"/>
        </radialGradient>
      </defs>
      <rect x="118" y="0" width="32" height="120" rx="12" fill="url(#silverTone)"/>
      <ellipse cx="134" cy="208" rx="134" ry="142" fill="url(#silverTone)"/>
    </svg>

    <svg class="hearts-band" role="img" aria-label="Decorative scattering of outlined hearts" viewBox="0 0 848 192" preserveAspectRatio="none">
      <defs>
        <linearGradient id="heartFadeX" x1="0" y1="0" x2="1" y2="0">
          <stop offset="0%" stop-color="var(--heart-grey)" stop-opacity="0"/>
          <stop offset="55%" stop-color="var(--heart-grey)" stop-opacity="0.35"/>
          <stop offset="100%" stop-color="var(--heart-grey)" stop-opacity="0.6"/>
        </linearGradient>
        <linearGradient id="heartFadeY" x1="0" y1="0" x2="0" y2="1">
          <stop offset="0%" stop-color="#fff" stop-opacity="0"/>
          <stop offset="60%" stop-color="#fff" stop-opacity="1"/>
        </linearGradient>
        <mask id="heartMask">
          <rect x="0" y="0" width="848" height="192" fill="url(#heartFadeY)"/>
        </mask>
      </defs>
      <rect x="0" y="0" width="848" height="192" fill="url(#heartFadeX)" mask="url(#heartMask)"/>
    </svg>
  </section>
</main>
</body>
</html>
```